Moon Tot needs ecommerce website design help

We need someone to set up a fully functional website for us. We sell baby bibs, I attached them along with our company logo (MTG: moon tot goods). The bibs are made of 100% silicon, they are safe, light weight, soft, smooth, flexible, dishwasher safe and has funny faces.

Business name: Moon Tot Goods
Elm Hollow, NY 11854
email: MoonTotGoods@mailexample.test
tel.: (631) 555-0147
website: MoonTotGoods.example

Target Market(s)

18-40

Industry/Entity Type

Baby

Coding

Coded - Design and coding required

Number of Pages Required

5+ page

Requirements
Must have
• 1. Pages: Why buy from us, Contact Us, Home page, Products Page, Blog
• 2. Use the colors from our logo for the web design.
• 3. Need a link that will connect visitors to our facebook, instagram, Pinterest and Tumblr account. Would like links on,the top left side of the page
Nice to have
• My Cart page
• 1. On contact us page, we want to include some type of template for the customer to complete. (Ex: name, email address, contact number, optional home address, comments)
• 2. When clients visit our website, we want a capture/pop up for the customer to subscribe to our email list to receive discounts. (Ex. Want 10% off your next order ? Suscribe to our mailing list below and get a 10% off code to use at check out. If they don't want to subscribe, they have the option to select "No Thank You, I want to pay full price).
• 3. On home page have subscribe to our email list.

```html
<!DOCTYPE html>
<html lang="en">
<head>
<meta charset="utf-8">
<title>Moon Tot Goods</title>
<link rel="stylesheet" href="https://fonts.googleapis.com/css2?family=Open+Sans:wght@400;600&family=Comic+Neue:wght@700&display=swap">
<style>
:root{
  --crimson:#8a2139;
  --crimson-btn:#c0213f;
  --rose:#f0506a;
  --lime:#a3cd1c;
  --olive:#8fb11a;
  --amber:#e8a33a;
  --ink:#333333;
  --muted:#666666;
  --paper:#f4f4f4;
  --field:#e4e4e4;
  --page:#ffffff;
  --topbar-text:#f3d9df;
  --icon:#d7c4c8;
}
*{box-sizing:border-box;margin:0;padding:0}
html,body{width:1200px;height:581px;overflow:hidden}
body{position:relative;background:var(--page);font-family:"Open Sans",sans-serif;color:var(--ink)}
.topbar{position:absolute;left:0;top:0;width:1200px;height:30px;background:var(--crimson);color:var(--topbar-text);font-size:10px}
.topbar .item{position:absolute;top:0;height:30px;display:flex;align-items:center;gap:6px;white-space:nowrap}
.social{position:absolute;left:178px;top:9px;display:flex;gap:7px}
.social a{display:block;width:13px;height:13px;background:var(--icon);border-radius:2px}
.site-header{position:absolute;left:0;top:30px;width:1200px;height:84px;background:#fff;border-bottom:1px solid #e6e6e6}
.brand{position:absolute;left:180px;top:24px;display:flex;align-items:center;gap:8px;font-family:"Comic Neue",cursive;font-weight:700;font-size:34px;color:var(--olive)}
.brand .dot{width:22px;height:22px;border-radius:50%;background:var(--crimson-btn)}
.nav{position:absolute;top:36px;font-size:11px;letter-spacing:.3px;color:#444;white-space:nowrap}
.nav.active{color:var(--crimson-btn)}
.sep{position:absolute;top:37px;width:1px;height:12px;background:#bbb}
.search{position:absolute;left:986px;top:24px;width:34px;height:32px;background:var(--amber);display:flex;align-items:center;justify-content:center}
.hero{position:absolute;left:0;top:115px;width:1200px;height:466px;background:linear-gradient(180deg,#fbfbfb,#f2f1ee)}
.hero-photo{position:absolute;left:540px;top:0;width:480px;height:430px;background:radial-gradient(ellipse at 60% 55%,#e8d6c8 0%,#e9eadf 45%,rgba(245,245,242,0) 75%)}
.hero-kicker{position:absolute;left:176px;top:119px;font-size:22px;font-weight:600;color:#444;white-space:nowrap}
.hero-title{position:absolute;left:177px;top:158px;font-family:"Comic Neue",cursive;font-weight:700;font-size:29px;letter-spacing:1px;white-space:nowrap}
.hero-title .green{color:var(--olive)}
.hero-title .red{color:var(--crimson-btn)}
.hero-cta{position:absolute;left:179px;top:217px;width:153px;height:34px;background:var(--crimson-btn);color:#fff;font-size:12px;display:flex;align-items:center;justify-content:center;letter-spacing:.3px}
.pager{position:absolute;left:580px;top:443px;display:flex;gap:6px}
.pager span{width:9px;height:9px;border-radius:50%;background:#999}
.pager span.on{background:var(--crimson-btn)}
.backdrop{position:absolute;inset:0;background:rgba(110,110,110,.32)}
.modal{position:absolute;left:342px;top:160px;width:516px;height:310px;background:var(--paper)}
.modal-close{position:absolute;left:846px;top:153px;width:19px;height:19px;border-radius:50%;background:#fff;border:2px solid #111;display:flex;align-items:center;justify-content:center;font-size:13px;font-weight:600;line-height:1;color:#111}
.modal-art{position:absolute;left:312px;top:68px;width:152px;height:196px;border-radius:46% 46% 40% 40%;background:radial-gradient(circle at 50% 60%,#ffb326,#f29a0e 70%,#e88a08)}
.modal-title{position:absolute;left:460px;top:225px;font-family:"Comic Neue",cursive;font-weight:700;font-size:25px;color:var(--rose);letter-spacing:.6px;white-space:nowrap}
.modal-text{position:absolute;left:463px;top:263px;width:370px;font-size:14px;line-height:16px;color:var(--ink)}
.email-field{position:absolute;left:462px;top:318px;width:336px;height:31px;background:var(--field);padding-left:11px;display:flex;align-items:center;font-size:11px;color:#888}
.subscribe{position:absolute;left:463px;top:366px;width:90px;height:29px;background:var(--lime);color:#fff;font-size:14px;display:flex;align-items:center;justify-content:center}
.decline{position:absolute;left:463px;top:423px;font-size:13px;color:var(--ink);white-space:nowrap}
</style>
</head>
<body>
<div class="topbar">
  <div class="social"><a aria-label="Social profile link"></a><a aria-label="Social profile link"></a><a aria-label="Social profile link"></a><a aria-label="Social profile link"></a></div>
  <div class="item" style="left:302px">
    <svg width="9" height="9" viewBox="0 0 24 24" fill="#d7c4c8"><path d="M6.6 10.8a15 15 0 0 0 6.6 6.6l2.2-2.2c.3-.3.7-.4 1-.2 1.1.4 2.3.6 3.6.6.6 0 1 .4 1 1V20c0 .6-.4 1-1 1A17 17 0 0 1 3 4c0-.6.4-1 1-1h3.5c.6 0 1 .4 1 1 0 1.3.2 2.5.6 3.6.1.3 0 .7-.2 1z"/></svg>
    <span>(631) 555-0147</span>
  </div>
  <div class="item" style="left:408px">
    <svg width="10" height="8" viewBox="0 0 20 16" fill="#d7c4c8"><path d="M0 0h20v16H0z" opacity=".9"/><path d="M0 0l10 8 10-8" stroke="#8a2139" stroke-width="1.6" fill="none"/></svg>
    <span>MoonTotGoods@mailexample.test</span>
  </div>
  <div class="item" style="left:816px">
    <svg width="9" height="10" viewBox="0 0 18 20" fill="#d7c4c8"><circle cx="9" cy="5" r="5"/><path d="M0 20c0-6 4-8 9-8s9 2 9 8z"/></svg>
    <span>Log in or Register</span>
  </div>
  <div class="item" style="left:944px">
    <svg width="11" height="10" viewBox="0 0 22 20" fill="#d7c4c8"><path d="M0 1h4l3 11h12l3-9H6" stroke="#d7c4c8" stroke-width="2" fill="none"/><circle cx="9" cy="17" r="2"/><circle cx="17" cy="17" r="2"/></svg>
    <span>(0)</span>
  </div>
</div>

<header class="site-header">
  <div class="brand"><span>MTG</span><span class="dot"></span></div>
  <span class="nav active" style="left:493px">HOME</span>
  <span class="sep" style="left:546px"></span>
  <span class="nav" style="left:570px">WHY BUY FROM US</span>
  <span class="sep" style="left:692px"></span>
  <span class="nav" style="left:714px">OUR PRODUCTS</span>
  <span class="sep" style="left:819px"></span>
  <span class="nav" style="left:840px">BLOG</span>
  <span class="sep" style="left:890px"></span>
  <span class="nav" style="left:912px">CONTACT</span>
  <div class="search">
    <svg width="12" height="12" viewBox="0 0 20 20" fill="none" stroke="#fff" stroke-width="2.6"><circle cx="8" cy="8" r="6"/><path d="M12.5 12.5L18 18"/></svg>
  </div>
</header>

<section class="hero">
  <div class="hero-photo" role="img" aria-label="Toddler sitting on the floor wearing an orange silicone bib"></div>
  <p class="hero-kicker">100% silicone bibs</p>
  <p class="hero-title"><span class="green">SAFE</span> <span class="red">LIGHT WEIGHT</span></p>
  <div class="hero-cta">GET FOR YOUR BABY</div>
  <div class="pager"><span></span><span class="on"></span><span></span></div>
</section>

<div class="backdrop"></div>

<div class="modal"></div>
<div class="modal-art" role="img" aria-label="Orange silicone bib with a playful tiger design"></div>
<div class="modal-close">×</div>
<h2 class="modal-title">Want 10% off your next order ?</h2>
<p class="modal-text">Subscribe to our mailing list below and get a 10% off code to use at check out</p>
<div class="email-field">Enter your mail id...</div>
<div class="subscribe">Subscribe</div>
<p class="decline">"No, Thank You. I want to pay full price”</p>
</body>
</html>
```